Ledgerwise Business Card Design

Business Card Design for new business called Ledgerwise focused on selling business software to small and medium size companies who have outgrown Tallyhouse. Similar companies would be Tallyhouse, Vemo, BrightCore. Also Dealharbor would be good to look at for additional ideas around look and feel.

Target Market(s)

Business to Business

Industry/Entity Type

Information Technology

Contact Information for Business Card

Standard Business Card Information

Font styles to use
Sans Serif

```html
<!DOCTYPE html>
<html lang="en">
<head>
<meta charset="utf-8">
<title>Ledgerwise Business Card</title>
<link rel="stylesheet" href="https://fonts.googleapis.com/css2?family=Montserrat:wght@500;700;800&display=swap">
<style>
  :root {
    --navy: #1b4f82;
    --orange: #ee7d27;
    --card-grey: #e8e8e8;
    --backdrop: #f1f1f1;
    --white: #ffffff;
  }
  * { margin: 0; padding: 0; box-sizing: border-box; }
  html, body {
    width: 1200px; height: 1200px; overflow: hidden;
    background: var(--backdrop);
    font-family: "Montserrat", Arial, sans-serif;
  }
  .canvas { position: relative; width: 1200px; height: 1200px; }
  .card {
    position: absolute; left: 150px; width: 900px; height: 514px;
    overflow: hidden; box-shadow: 0 6px 22px rgba(0,0,0,.12);
  }
  .card-front { top: 60px; background: var(--navy); }
  .card-back { top: 630px; background: var(--card-grey); }
  .card svg.shapes { position: absolute; inset: 0; }

  .brand {
    position: absolute; display: flex; align-items: center; gap: 14px;
    font-weight: 800; letter-spacing: 1px; text-transform: uppercase;
    white-space: nowrap;
  }
  .brand-dot { border-radius: 50%; background: var(--orange); flex: none; }
  .card-front .brand { left: 250px; top: 222px; font-size: 54px; color: var(--white); }
  .card-front .brand-dot { width: 52px; height: 52px; }
  .card-back .brand { right: 40px; top: 296px; font-size: 30px; color: var(--navy); }
  .card-back .brand-dot { width: 32px; height: 32px; }

  .name-tag {
    position: absolute; left: 330px; top: 46px; width: 330px; height: 56px;
    color: var(--white); text-transform: uppercase;
  }
  .name-tag .name { position: absolute; right: 40px; top: 8px; font-size: 21px; font-weight: 500; }
  .name-tag .role { position: absolute; right: 40px; top: 33px; font-size: 13px; text-transform: none; }

  .contact-list {
    position: absolute; left: 48px; top: 170px; list-style: none;
    color: var(--white); font-size: 19px; font-weight: 500;
  }
  .contact-list li { display: flex; align-items: center; gap: 16px; height: 56px; }
  .contact-list .icon {
    width: 34px; height: 34px; border-radius: 50%; background: var(--orange);
    display: flex; align-items: center; justify-content: center; flex: none;
  }
  .contact-list .address { font-size: 16px; line-height: 1.25; }
</style>
</head>
<body>
<main class="canvas">

  <section class="card card-front" aria-label="Business card front">
    <svg class="shapes" width="900" height="514" viewBox="0 0 900 514">
      <polygon points="400,0 900,0 900,514 740,514" fill="var(--orange)"/>
    </svg>
    <div class="brand"><span class="brand-dot"></span>Ledgerwise</div>
  </section>

  <section class="card card-back" aria-label="Business card back">
    <svg class="shapes" width="900" height="514" viewBox="0 0 900 514">
      <polygon points="0,0 270,0 690,514 0,514" fill="var(--navy)"/>
      <polygon points="330,46 660,46 690,102 370,102" fill="var(--orange)"/>
    </svg>
    <div class="name-tag"><span class="name">Name Surname</span><span class="role">Role</span></div>

    <ul class="contact-list">
      <li><span class="icon"><svg width="16" height="20" viewBox="0 0 16 20"><rect x="2" y="1" width="12" height="18" rx="2" fill="none" stroke="#fff" stroke-width="2"/><circle cx="8" cy="15.5" r="1.3" fill="#fff"/></svg></span>+00 21 0300 4419</li>
      <li><span class="icon"><svg width="20" height="18" viewBox="0 0 20 18"><path d="M2 6c0-3 16-3 16 0v2h-4V6H6v2H2z" fill="#fff"/><rect x="4" y="9" width="12" height="8" rx="1.5" fill="#fff"/></svg></span>+00 21 1234 4420</li>
      <li><span class="icon"><svg width="20" height="14" viewBox="0 0 20 14"><rect x="1" y="1" width="18" height="12" fill="none" stroke="#fff" stroke-width="2"/><path d="M1 1l9 7 9-7" fill="none" stroke="#fff" stroke-width="2"/></svg></span>info@ledgerwise.com</li>
      <li><span class="icon"><svg width="20" height="20" viewBox="0 0 20 20"><circle cx="10" cy="10" r="8" fill="none" stroke="#fff" stroke-width="2"/><ellipse cx="10" cy="10" rx="3.5" ry="8" fill="none" stroke="#fff" stroke-width="1.6"/><path d="M2 10h16" stroke="#fff" stroke-width="1.6"/></svg></span>www.ledgerwise.com</li>
      <li><span class="icon"><svg width="16" height="20" viewBox="0 0 16 20"><path d="M8 19s7-7 7-11A7 7 0 0 0 1 8c0 4 7 11 7 11z" fill="#fff"/><circle cx="8" cy="8" r="2.5" fill="var(--orange)"/></svg></span><span class="address">Street # 6, Road Lorem Ipsum<br>City, Region, Country, Postal Code</span></li>
    </ul>

    <div class="brand"><span class="brand-dot"></span>Ledgerwise</div>
  </section>

</main>
</body>
</html>
```